Copper Ridge Inquiries Letterhead

I would like to design a letterhead for a private investigation company. Our primary clients will be law firms. The business card is included below

```html
<!DOCTYPE html>
<html lang="en">
<head>
<meta charset="utf-8">
<title>Copper Ridge Inquiries Letterhead</title>
<link href="https://fonts.googleapis.com/css2?family=Montserrat:wght@400;500;700;800&family=Lato:wght@400;700&family=Italianno&display=swap" rel="stylesheet">
<style>
  :root {
    --navy: #1b3563;
    --orange: #f06135;
    --ink: #1d1d1f;
    --paper: #ffffff;
    --backdrop: #e7e8ea;
    --muted: #c9d2e3;
  }
  * { box-sizing: border-box; margin: 0; padding: 0; }
  html, body { width: 1200px; height: 960px; overflow: hidden; }
  body {
    background: var(--backdrop);
    font-family: "Lato", Arial, sans-serif;
    color: var(--ink);
    position: relative;
  }
  .letterhead {
    position: absolute;
    left: 270px; top: 40px;
    width: 660px; height: 880px;
    background: var(--paper);
    overflow: hidden;
    box-shadow: 0 4px 18px rgba(0,0,0,0.12);
  }
  .masthead {
    height: 150px;
    background: var(--navy);
    display: flex;
    align-items: center;
    padding: 0 40px;
  }
  .brand {
    display: flex;
    align-items: center;
    gap: 12px;
  }
  .brand-dot {
    width: 34px; height: 34px;
    border-radius: 50%;
    background: var(--orange);
    flex: none;
  }
  .brand-name {
    font-family: "Montserrat", Arial, sans-serif;
    font-weight: 800;
    color: var(--paper);
    font-size: 20px;
    line-height: 1.1;
    letter-spacing: 0.5px;
    text-transform: uppercase;
  }
  .divider {
    width: 2px; height: 54px;
    background: var(--orange);
    margin: 0 26px 0 auto;
  }
  .contact {
    list-style: none;
    font-family: "Montserrat", Arial, sans-serif;
    font-size: 10.5px;
    color: var(--muted);
    letter-spacing: 0.6px;
    text-transform: uppercase;
    line-height: 1.65;
    margin-right: 10px;
  }
  .contact li { display: flex; align-items: center; gap: 7px; }
  .contact svg { width: 10px; height: 10px; flex: none; }
  .contact .no-icon { padding-left: 17px; }

  .letter-body {
    padding: 44px 56px 0 64px;
    font-size: 13px;
    line-height: 1.45;
  }
  .date { margin-bottom: 16px; }
  .recipient { margin-bottom: 14px; }
  .salutation {
    font-family: "Montserrat", Arial, sans-serif;
    font-weight: 700;
    font-size: 17px;
    margin: 6px 0 16px;
  }
  .letter-body p.para { margin-bottom: 16px; max-width: 520px; }
  .closing { margin-top: 22px; }
  .signature {
    font-family: "Italianno", cursive;
    font-size: 48px;
    margin-top: 18px;
    line-height: 1;
  }
  .corner-sweep {
    position: absolute;
    left: 0; bottom: 0;
    width: 660px; height: 320px;
  }
</style>
</head>
<body>
  <article class="letterhead">
    <header class="masthead">
      <div class="brand">
        <span class="brand-dot"></span>
        <span class="brand-name">Copper Ridge<br>Inquiries</span>
      </div>
      <span class="divider"></span>
      <ul class="contact">
        <li><svg viewBox="0 0 10 10"><path d="M5 0.5a3.2 3.2 0 0 0-3.2 3.2C1.8 6 5 9.5 5 9.5S8.2 6 8.2 3.7A3.2 3.2 0 0 0 5 0.5zm0 4.5a1.3 1.3 0 1 1 0-2.6 1.3 1.3 0 0 1 0 2.6z" fill="#f06135"/></svg>Marble Bend, TX</li>
        <li><svg viewBox="0 0 10 10"><path d="M2.3 0.8l1.6 1.9-.9 1.2c.6 1.3 1.6 2.3 2.9 2.9l1.2-.9 1.9 1.6-.9 1.6C4.3 9.2.8 5.7.7 1.7z" fill="#f06135"/></svg>210.555.0142</li>
        <li><svg viewBox="0 0 10 10"><rect x="0.8" y="2" width="8.4" height="6" rx="0.8" fill="#f06135"/><path d="M1.2 2.5L5 5.4l3.8-2.9" stroke="#1b3563" stroke-width="0.9" fill="none"/></svg>dana@copperridgeinquiries.com</li>
        <li class="no-icon">License No. 04721936</li>
      </ul>
    </header>

    <section class="letter-body">
      <p class="date">January-03-2020</p>
      <p class="recipient">Mr, John Doe<br>President</p>
      <p class="recipient">Harbor Legal Group<br>123 Street Name, Suite# 10<br>City, State, 120023</p>
      <p class="salutation">Dear Mr, John</p>
      <p class="para">Lorem ipsum dolor sit amet, consectetur adipiscing elit, sed do eiusmod tempor incididunt ut labore et dolore magna aliqua. Ut enim ad minim veniam, quis nostrud exercitation ullamco laboris nisi ut aliquip ex ea commodo consequat. Duis aute irure dolor in reprehenderit in voluptate velit esse cillum dolore eu fugiat nulla pariatur.</p>
      <p class="para">Lorem ipsum dolor sit amet, consectetur adipiscing elit, sed do eiusmod tempor incididunt ut labore et dolore magna aliqua. Ut enim ad minim veniam, quis nostrud exercitation ullamco laboris nisi ut aliquip ex ea commodo consequat. Duis aute irure dolor in reprehenderit in voluptate velit esse cillum dolore eu fugiat nulla pariatur.</p>
      <p class="para">Lorem ipsum dolor sit amet, consectetur adipiscing elit, sed do eiusmod tempor incididunt ut labore et dolore magna aliqua. Ut enim ad minim veniam, quis nostrud exercitation ullamco laboris nisi ut aliquip ex ea commodo consequat.</p>
      <p class="para">Excepteur sint occaecat cupidatat non proident, sunt in culpa qui officia deserunt mollit anim id est laborum. re et dolore magnam aliquam quaerat voluptatem.</p>
      <p class="closing">Regards</p>
      <p class="signature">Laura Bennett</p>
    </section>

    <svg class="corner-sweep" viewBox="0 560 660 320" preserveAspectRatio="none" aria-hidden="true">
      <path d="M300 880 C 420 770, 540 690, 660 620 L 660 628 C 560 700, 450 780, 350 880 Z" fill="#1b3563"/>
      <path d="M372 880 C 470 790, 560 720, 660 652 L 660 880 Z" fill="#f06135"/>
    </svg>
  </article>
</body>
</html>
```